Banner Ad Design Project

We need a 728x90 and a 300x250
1st option
"I have a lead for you. Click here to close the deal."
In large bold letters.
Under this in smaller letters,
"Borwelt. For serious business networkers"
2nd option
"Put that coffee down!"
"Coffee's for closers only."
Close more deals. BORWELT LOGO
(this is a quote from Harrowmere Tavish. It is a famous sales movie)
The other option is
"First you get the money" "Then you get the power" in bold letters.
"Borwelt. For serious business networkers" in smaller letters at the bottom.
-Must have our colors
-Must have our logo (Small at the bottom right)
-Watch the video at borwelt () com
Please be creative. If the banner can have multiple images that would be great as well.
This needs to be a serious looking ad that is bold and clean.
Updates
Please be sure to use the phrase, "Put that coffee down! Coffee's for closers only" with the logo and at the bottom the words, Borwelt, for serious business networkers. in one of the designs. This will be our first campaign. I am looking for a very simple design that is bold. Perhaps just a coffee cup with the words and no other graphics.
Target Market(s)
Sales professionals
Industry/Entity Type
Business
Look and feel

```html
<!DOCTYPE html>
<html lang="en">
<head>
<meta charset="utf-8">
<title>Borwelt banner set</title>
<link rel="stylesheet" href="https://fonts.googleapis.com/css2?family=Open+Sans:wght@400;600;700&display=swap">
<style>
  :root {
    --stage-light: #d6d6d6;
    --stage-mid: #a9a9a9;
    --stage-dark: #7a7a7a;
    --ink-white: #ffffff;
    --photo-dark: #1c0d06;
    --photo-brown: #4a2210;
    --photo-red: #7a2a12;
    --photo-amber: #a2541c;
    --cup-white: #e9e6e1;
    --button-top: #ffe14a;
    --button-bottom: #f2a200;
    --button-ink: #1a1a1a;
    --brand-blue: #2f5fa5;
    --brand-orange: #f3a21b;
    --panel-white: #ffffff;
  }
  * { margin: 0; padding: 0; box-sizing: border-box; }
  html, body { width: 1200px; height: 727px; overflow: hidden; }
  body {
    font-family: "Open Sans", Arial, sans-serif;
    background: radial-gradient(ellipse at 30% 40%, var(--stage-light) 0%, var(--stage-mid) 55%, var(--stage-dark) 100%);
    position: relative;
  }
  .banner { position: absolute; overflow: hidden; color: var(--ink-white); }
  .banner--square { top: 57px; width: 447px; height: 372px; }
  .banner--square.first { left: 134px; }
  .banner--square.second { left: 601px; }
  .banner--leader { left: 60px; top: 475px; width: 1083px; height: 134px; }

  .photo {
    position: absolute; inset: 0;
    background:
      radial-gradient(ellipse 34% 26% at 66% 62%, var(--cup-white) 0%, rgba(233,230,225,0.55) 55%, rgba(233,230,225,0) 100%),
      radial-gradient(circle at 85% 20%, var(--photo-amber) 0%, rgba(162,84,28,0) 35%),
      radial-gradient(circle at 15% 30%, var(--photo-red) 0%, rgba(122,42,18,0) 40%),
      linear-gradient(180deg, var(--photo-dark) 0%, var(--photo-brown) 60%, var(--photo-dark) 100%);
  }
  .banner--leader .photo {
    left: 141px;
    background:
      radial-gradient(ellipse 14% 60% at 50% 80%, var(--cup-white) 0%, rgba(233,230,225,0.4) 55%, rgba(233,230,225,0) 100%),
      radial-gradient(circle at 80% 30%, var(--photo-amber) 0%, rgba(162,84,28,0) 30%),
      linear-gradient(90deg, var(--photo-dark) 0%, var(--photo-brown) 50%, var(--photo-dark) 100%);
  }

  .headline, .subline, .tagline { position: absolute; white-space: nowrap; line-height: 1; }
  .headline { font-weight: 700; font-size: 35px; letter-spacing: -0.3px; }
  .subline { font-weight: 400; font-size: 30px; letter-spacing: -0.3px; }
  .tagline { font-weight: 400; font-size: 18.5px; }

  .banner--square .headline { left: 0; right: 0; text-align: center; top: 11px; }
  .banner--square .subline { left: 0; right: 0; text-align: center; top: 52px; }
  .banner--square .tagline { left: 0; right: 0; text-align: center; top: 96px; }

  .banner--leader .headline { left: 160px; top: 12px; font-size: 34px; }
  .banner--leader .subline { left: 173px; top: 53px; font-size: 29.5px; }
  .banner--leader .tagline { left: 168px; top: 95px; font-size: 18.3px; }

  .brand {
    position: absolute; display: flex; flex-direction: column; align-items: center; gap: 6px;
    font-weight: 700; font-size: 20px; line-height: 1; color: var(--brand-orange);
  }
  .brand__mark { width: 56px; height: 56px; background: var(--brand-blue); }
  .banner--square .brand { left: 22px; top: 206px; width: 104px; }
  .brand-panel {
    position: absolute; left: 0; top: 0; width: 141px; height: 134px;
    background: var(--panel-white); display: flex; align-items: center; justify-content: center;
  }
  .brand-panel .brand { position: static; }
  .brand-panel .brand__mark { width: 40px; height: 40px; }

  .cta {
    position: absolute; width: 189px; height: 49px;
    border-radius: 4px;
    background: linear-gradient(180deg, var(--button-top) 0%, var(--button-bottom) 100%);
    display: flex; align-items: center; justify-content: space-between;
    padding: 0 10px 0 14px;
    color: var(--button-ink); font-weight: 600; font-size: 20px;
  }
  .banner--square .cta { left: 127px; top: 309px; }
  .banner--leader .cta { left: 876px; top: 57px; width: 188px; height: 48px; }
  .cta svg { width: 32px; height: 32px; }
</style>
</head>
<body>

  <section class="banner banner--square first">
    <div class="photo" role="img" aria-label="Photograph of a white coffee cup on a saucer in a warm, dimly lit café"></div>
    <p class="headline">PUT THAT COFFEE DOWN!</p>
    <p class="subline">COFFEE'S FOR CLOSERS ONLY</p>
    <p class="tagline">BORWELT. FOR SERIOUSBUSINESS NETWORKERS</p>
    <div class="brand"><span class="brand__mark"></span>borwelt</div>
    <a class="cta">Learn More!
      <svg viewBox="0 0 32 32"><circle cx="16" cy="16" r="14" fill="#ffffff" stroke="#555" stroke-width="1.5"/><path d="M13 9l7 7-7 7" fill="none" stroke="#1a1a1a" stroke-width="3.5" stroke-linecap="round" stroke-linejoin="round"/></svg>
    </a>
  </section>

  <section class="banner banner--square second">
    <div class="photo" role="img" aria-label="Photograph of a white coffee cup on a saucer in a warm, dimly lit café"></div>
    <p class="headline">PUT THAT COFFEE DOWN!</p>
    <p class="subline">COFFEE'S FOR CLOSERS ONLY</p>
    <p class="tagline">BORWELT. FOR SERIOUSBUSINESS NETWORKERS</p>
    <div class="brand"><span class="brand__mark"></span>borwelt</div>
    <a class="cta">Learn More!
      <svg viewBox="0 0 32 32"><circle cx="16" cy="16" r="14" fill="#ffffff" stroke="#555" stroke-width="1.5"/><path d="M13 9l7 7-7 7" fill="none" stroke="#1a1a1a" stroke-width="3.5" stroke-linecap="round" stroke-linejoin="round"/></svg>
    </a>
  </section>

  <section class="banner banner--leader">
    <div class="brand-panel">
      <div class="brand"><span class="brand__mark"></span>borwelt</div>
    </div>
    <div class="photo" role="img" aria-label="Photograph of a white coffee cup in a dark café setting"></div>
    <p class="headline">PUT THAT COFFEE DOWN!</p>
    <p class="subline">COFFEE'S FOR CLOSERS ONLY</p>
    <p class="tagline">BORWELT. FOR SERIOUSBUSINESS NETWORKERS</p>
    <a class="cta">Learn More!
      <svg viewBox="0 0 32 32"><circle cx="16" cy="16" r="14" fill="#ffffff" stroke="#555" stroke-width="1.5"/><path d="M13 9l7 7-7 7" fill="none" stroke="#1a1a1a" stroke-width="3.5" stroke-linecap="round" stroke-linejoin="round"/></svg>
    </a>
  </section>

</body>
</html>
```